A products line website

Design theme: Corporate, elegant, neat, clean and warm and containing the following pages:
1. About Tarvelle lightening collection
2. Side banner(s) in home page for internal promotions, e.g.: New product, new designs, exhibitions, etc.)
3. Product catalogue that could be classified based on two level classification
4. Crystal quality
5. Lightening projects, few words about the lightening project and a link to the special design chandelier projects website
6. Special design chandeliers
a. About Special Design Chandeliers Projects containing:
i. Tarvelle Design dpt.
ii. Safety factors
iii. Artists (designer’s names)
iv. Ability to produce any chandelier size
b. Projects showcase, A study case with detailed photos and videos if possible about successful lightening projects from entire world, classified by type (Hotels, Banks, Religious bldgs...etc.)
c. Interior Design Firms
d. Request a Special Design
7. All the general requirements

Requirements
Must have
• The design should include a home webpage and an internal page design. The design should fullfill the following requriements:

1. Strictly follow the corporate identity materials guidelines - see attachment
2. Supports multi-language
3. User can change between languages using flags
4. Web surfer can optionally change the default language
5. An integrated live chat push button for ChatBrindo
8. Site Header should contain the following information:
a. Logo
b. Slogan
c. Links to site pages
d. Link to the home page
e. Link to the landing page
f. A language option drop box
9. Footers should have:
a. Links to all other 5 websites in a dropbox form
b. Link to privacy statement
c. Link to copyright notice
d. Link to sitemap
e. Newsletter subscription one field form
11. A universal customer service section that offer the following services:
a. Links to end user installation manuals
b. Links to products cleaning and maintenance guide
c. Customer complaints center
12. A news sub-section that should contain:
a. Latest product and promotional announcements
b. Corporate news
c. Exhibitions coverage
13. A link to tarvelle Worldwide:
a. A database driven interactive map reflecting Tarvelle list of agents and distributors worldwide with list of supported products this interactive map could be limited in every sub-site for specific line of product
b. Capture potential resellers and agents
c. Become a partner form

```html
<!DOCTYPE html>
<html lang="en">
<head>
<meta charset="utf-8">
<title>Tarvelle Crystal</title>
<link rel="stylesheet" href="https://fonts.googleapis.com/css2?family=Didact+Gothic&family=Open+Sans:wght@400;600&display=swap">
<style>
:root{
  --page:#1f1e31;
  --panel:#2a2942;
  --panel-line:#4a4970;
  --band-from:#44447a;
  --ink-light:#e6e6ee;
  --ink-soft:#b9b8c8;
  --ink-dim:#9d9cb2;
  --accent:#8c8ad6;
  --link-top:#3d3aa8;
  --footer:#000000;
  --bottom:#3e3b66;
  --white:#ffffff;
  --frame:#6c6ca6;
}
*{box-sizing:border-box;margin:0;padding:0}
html,body{width:1200px;height:2169px;overflow:hidden}
body{position:relative;background:var(--page);font-family:"Open Sans",Arial,sans-serif;color:var(--ink-soft)}
.abs{position:absolute}

/* header */
.site-header{position:absolute;left:0;top:0;width:1200px;height:212px;background:linear-gradient(#ffffff,#e4e4e6 78%,#d6d6d8)}
.logo-box{position:absolute;left:49px;top:16px;width:204px;height:147px;background:linear-gradient(#2b2828,#171414);border-radius:8px;display:flex;flex-direction:column;align-items:center;justify-content:flex-end;padding-bottom:30px}
.logo-mark{width:22px;height:22px;border-radius:50%;background:#e9e9e9;margin-bottom:14px}
.logo-name{font-family:"Didact Gothic",sans-serif;color:#f2f2f2;font-size:25px;letter-spacing:5px}
.top-links{position:absolute;right:30px;top:26px;font-size:14px;color:var(--link-top)}
.top-links span{padding:0 7px}
.top-links .sep{color:#777;padding:0}
.lang-select{position:absolute;left:1008px;top:63px;width:163px;height:29px;background:#fff;border:1px solid #c9c9c9;font-size:14px;color:#222;padding:5px 12px}
.lang-select .arrow{position:absolute;right:0;top:0;width:30px;height:27px;background:#7c7c7c}
.lang-select .arrow::after{content:"";position:absolute;left:10px;top:11px;border-left:5px solid transparent;border-right:5px solid transparent;border-top:6px solid #fff}
.main-nav{position:absolute;left:416px;top:168px;width:784px;height:44px;background:#fff;display:flex;align-items:center;font-size:17px;color:#222}
.main-nav a{position:absolute;top:11px;text-decoration:none;color:#222}

/* hero */
.hero{position:absolute;left:45px;top:217px;width:1115px;height:372px;border:2px solid var(--frame);background:linear-gradient(90deg,#141530 0%,#263566 35%,#7d8fc4 55%,#3b4b8c 75%,#15173a 100%)}
.hero-title{position:absolute;left:36px;top:74px;font-family:"Didact Gothic",sans-serif;font-size:31px;color:#fff;letter-spacing:1px}
.hero-text{position:absolute;left:36px;top:128px;width:390px;font-size:17px;line-height:28px;color:#eef}

/* section bands */
.band{position:absolute;height:29px;background:linear-gradient(90deg,var(--band-from),rgba(68,68,122,0));font-family:"Didact Gothic",sans-serif;font-size:17px;color:var(--white);padding:4px 9px;letter-spacing:.3px}
.band.right{background:linear-gradient(90deg,#5a5a8c,rgba(90,90,140,0));padding-left:17px}

.photo{position:absolute;border:2px solid var(--frame)}
.photo.chess{background:linear-gradient(135deg,#2a3760,#7a8fc0 45%,#1f2748)}
.photo.crystal{background:linear-gradient(135deg,#3b4a86,#9eb0e0 50%,#28306a)}
.photo.gold{background:radial-gradient(circle at 50% 45%,#e9c46a,#8a6420 45%,#141216 80%)}
.photo.bronze{background:radial-gradient(circle at 50% 45%,#f0d3a8,#8b5b3a 45%,#19151a 80%)}
.photo.silver{background:radial-gradient(circle at 50% 45%,#f4f4f6,#9fa4b0 45%,#4d5260 90%)}
.photo.clear{background:radial-gradient(circle at 50% 50%,#f3efe6,#b9ae9a 50%,#5a5246)}

.copy{position:absolute;font-size:12.5px;line-height:17.5px;color:var(--ink-soft)}
.more{position:absolute;font-family:"Didact Gothic",sans-serif;font-size:14px;color:#e9e9f0;letter-spacing:.6px;border-bottom:1px solid #8a89a8;padding-bottom:1px}
.rule{position:absolute;left:45px;top:941px;width:759px;height:1px;background:#3d3c58}

.card{position:absolute;width:218px;height:215px;border:2px solid var(--frame)}
.card-label{position:absolute;top:6px;left:0;width:100%;text-align:center;font-family:"Didact Gothic",sans-serif;font-size:23px;color:#fff;letter-spacing:.5px}
.check-btn{position:absolute;width:150px;height:28px;background:#050507;border-radius:5px;color:#fff;font-family:"Didact Gothic",sans-serif;font-size:13px;letter-spacing:1px;text-align:center;line-height:28px}

.service-art{position:absolute;width:120px;height:127px;border-radius:14px}
.service-label{position:absolute;top:1491px;font-size:14px;color:#eee}

.news-col{position:absolute;top:1599px;height:194px;background:var(--panel)}
.news-tab{position:absolute;top:1604px;font-family:"Didact Gothic",sans-serif;font-size:17px;color:var(--accent)}
.news-copy{position:absolute;font-size:11.5px;line-height:17px;color:var(--ink-dim)}

.thumb{position:absolute;width:104px;height:91px;border:2px solid #5c5b86}
.side-copy{position:absolute;left:958px;width:205px;font-size:12px;line-height:17.5px;color:var(--ink-dim)}

.email-field{position:absolute;background:#0b0b10;border:1px solid #55557a;color:#bdbdcc;font-size:12.5px;padding:4px 12px}
.social{position:absolute;top:1762px;width:41px;height:41px;border-radius:50%}

/* footer */
.site-footer{position:absolute;left:0;top:1861px;width:1200px;height:217px;background:var(--footer)}
.foot-title{position:absolute;top:1880px;font-family:"Didact Gothic",sans-serif;font-size:14px;color:#fff;letter-spacing:.6px}
.foot-copy{position:absolute;font-size:12px;line-height:20px;color:#c8c8d0}
.map{position:absolute;left:842px;top:1917px;width:226px;height:129px;background:linear-gradient(135deg,#e8e1d2,#f1ecdf 50%,#d9d3c4)}
.bottom-bar{position:absolute;left:0;top:2078px;width:1200px;height:91px;background:var(--bottom);text-align:center;color:#fff;font-size:12.5px}
</style>
</head>
<body>

<header class="site-header">
  <div class="logo-box"><span class="logo-mark"></span><span class="logo-name">TARVELLE</span></div>
  <div class="top-links"><span>Live chat</span><span class="sep">|</span><span>Register</span><span class="sep">|</span><span>Help</span></div>
  <div class="lang-select">English<span class="arrow"></span></div>
  <nav class="main-nav">
    <a style="left:29px">HOME</a>
    <a style="left:120px">FACILITIES</a>
    <a style="left:247px">MEDIA CENTER</a>
    <a style="left:417px">CAREERS</a>
    <a style="left:534px">ABOUT US</a>
    <a style="left:653px">CONTACT US</a>
  </nav>
</header>

<section class="hero" role="img" aria-label="Photograph of a cluster of clear quartz crystals">
  <h1 class="hero-title">SED EIUSMOD TEMPOR</h1>
  <p class="hero-text">Lorem ipsum dolor sit amet, consectetur adipisicing elit, sed do eiusmod tempor incididunt ut labore et dolore magna aliqua. Ut enim ad minim veniam, quis nostrud exercitation ullamco laboris nisi ut aliquip ex ea commodo consequat.</p>
</section>

<!-- about + special design -->
<h2 class="band" style="left:45px;top:611px;width:380px">ABOUT TARVELLE LIGHTENING COLLECTION</h2>
<h2 class="band" style="left:448px;top:611px;width:356px">SPECIAL DESIGN CHANDELIERS</h2>
<div class="photo chess" role="img" aria-label="Photograph of glass chess pieces on a board" style="left:60px;top:660px;width:333px;height:130px"></div>
<div class="photo crystal" role="img" aria-label="Photograph of a crystal cluster" style="left:450px;top:660px;width:334px;height:130px"></div>
<p class="copy" style="left:58px;top:803px;width:350px">Lorem ipsum dolor sit amet, consectetur adipisicing elit, sed do eiusmod tempor incididunt ut labore et dolore magna aliqua. Ut enim ad minim veniam, quis nostrud exercitation ullamco laboris nisi ut aliquip ex ea commodo consequat. Lorem ipsum dolor sit amet....</p>
<p class="copy" style="left:452px;top:803px;width:350px">Lorem ipsum dolor sit amet, consectetur adipisicing elit, sed do eiusmod tempor incididunt ut labore et dolore magna aliqua. Ut enim ad minim veniam, quis nostrud exercitation ullamco laboris nisi ut aliquip ex ea commodo consequat. Lorem ipsum dolor sit amet....</p>
<span class="more" style="left:307px;top:903px">READ MORE</span>
<span class="more" style="left:705px;top:903px">READ MORE</span>
<div class="rule"></div>

<!-- catalogue -->
<h2 class="band" style="left:45px;top:963px;width:380px">PRODUCT CATALOGUE</h2>
<div class="card photo bronze" role="img" aria-label="Photograph of a bronze crystal chandelier" style="left:56px;top:1016px"><span class="card-label">ADIPISICING</span></div>
<div class="card photo clear" role="img" aria-label="Close photograph of crystal droplets" style="left:302px;top:1016px"><span class="card-label">ADIPISICING</span></div>
<div class="card photo gold" role="img" aria-label="Photograph of a gold crystal chandelier" style="left:549px;top:1016px"><span class="card-label">ADIPISICING</span></div>
<div class="check-btn" style="left:94px;top:1239px">QUALITY CHECK</div>
<div class="check-btn" style="left:335px;top:1239px">QUALITY CHECK</div>
<div class="check-btn" style="left:583px;top:1239px">QUALITY CHECK</div>

<!-- customer service -->
<h2 class="band" style="left:45px;top:1301px;width:380px">UNIVERSAL CUSTOMER SERVICE</h2>
<div class="service-art" role="img" aria-label="Illustration of a user with a pencil" style="left:62px;top:1346px;background:radial-gradient(circle at 50% 55%,#3e8fd0,#f0b985 45%,rgba(31,30,49,0) 72%)"></div>
<div class="service-art" role="img" aria-label="Illustration of a blue guide book" style="left:322px;top:1346px;background:radial-gradient(circle at 50% 50%,#3d7fd6,#1d4f96 45%,rgba(31,30,49,0) 72%)"></div>
<div class="service-art" role="img" aria-label="Illustration of a support figure with a phone" style="left:560px;top:1346px;background:radial-gradient(circle at 50% 50%,#3fb6f2,#1b88d0 45%,rgba(31,30,49,0) 72%)"></div>
<span class="service-label" style="left:44px">User Installation Manuals</span>
<span class="service-label" style="left:283px">Products&nbsp; Maintenance Guide</span>
<span class="service-label" style="left:541px">Customer complaints center</span>

<!-- announcements -->
<h2 class="band" style="left:45px;top:1554px;width:380px">LATEST ANNOUNCEMENTS</h2>
<div class="news-col" style="left:45px;width:246px"></div>
<div class="news-col" style="left:304px;width:251px"></div>
<div class="news-col" style="left:564px;width:242px"></div>
<span class="news-tab" style="left:55px">Latest news</span>
<span class="news-tab" style="left:311px">Corporate news</span>
<span class="news-tab" style="left:571px">Exhibitions coverage</span>
<p class="news-copy" style="left:55px;top:1641px;width:232px">Lorem ipsum dolor sit amet, consect etur adipiscing elit, sed do eiusmod tempor incididunt ut labore et aliqua....</p>
<p class="news-copy" style="left:55px;top:1714px;width:232px">Lorem ipsum dolor sit amet, consect etur adipiscing elit, sed do eiusmod tempor incididunt ut labore et aliqua....</p>
<p class="news-copy" style="left:315px;top:1641px;width:232px">Lorem ipsum dolor sit amet, consect etur adipiscing elit, sed do eiusmod tempor incididunt ut labore et aliqua....</p>
<p class="news-copy" style="left:315px;top:1714px;width:232px">Lorem ipsum dolor sit amet, consect etur adipiscing elit, sed do eiusmod tempor incididunt ut labore et aliqua....</p>
<p class="news-copy" style="left:575px;top:1641px;width:228px">Lorem ipsum dolor sit amet, consect etur adipiscing elit, sed do eiusmod tempor incididunt ut magna aliqua....</p>
<p class="news-copy" style="left:575px;top:1714px;width:228px">Lorem ipsum dolor sit amet, consect etur adipiscing elit, sed do eiusmod tempor incididunt ut labore gra aliqua....</p>
<span class="more" style="left:716px;top:1796px">READ MORE</span>

<!-- right column -->
<h2 class="band right" style="left:837px;top:611px;width:329px">NEW PRODUCT</h2>
<div class="thumb photo bronze" role="img" aria-label="Chandelier photograph" style="left:840px;top:654px"></div>
<div class="thumb photo gold" role="img" aria-label="Chandelier photograph" style="left:950px;top:654px"></div>
<div class="thumb photo silver" role="img" aria-label="Chandelier photograph" style="left:1062px;top:654px"></div>
<div class="thumb photo bronze" role="img" aria-label="Chandelier photograph" style="left:840px;top:752px"></div>
<div class="thumb photo gold" role="img" aria-label="Chandelier photograph" style="left:950px;top:752px"></div>
<div class="thumb photo silver" role="img" aria-label="Chandelier photograph" style="left:1062px;top:752px"></div>
<span class="more" style="left:1075px;top:855px">READ MORE</span>

<h2 class="band right" style="left:837px;top:898px;width:329px">NEW DESIGN</h2>
<div class="thumb photo bronze" role="img" aria-label="Chandelier photograph" style="left:840px;top:940px"></div>
<div class="thumb photo gold" role="img" aria-label="Chandelier photograph" style="left:950px;top:940px"></div>
<div class="thumb photo silver" role="img" aria-label="Chandelier photograph" style="left:1062px;top:940px"></div>
<div class="thumb photo bronze" role="img" aria-label="Chandelier photograph" style="left:840px;top:1037px"></div>
<div class="thumb photo gold" role="img" aria-label="Chandelier photograph" style="left:950px;top:1037px"></div>
<div class="thumb photo silver" role="img" aria-label="Chandelier photograph" style="left:1062px;top:1037px"></div>
<span class="more" style="left:1075px;top:1140px">READ MORE</span>

<h2 class="band right" style="left:837px;top:1185px;width:329px">NEW DESIGN</h2>
<div class="thumb photo bronze" role="img" aria-label="Chandelier photograph" style="left:840px;top:1231px;height:86px"></div>
<div class="thumb photo gold" role="img" aria-label="Chandelier photograph" style="left:840px;top:1332px;height:86px"></div>
<div class="thumb photo silver" role="img" aria-label="Chandelier photograph" style="left:840px;top:1433px;height:90px"></div>
<p class="side-copy" style="top:1231px">Lorem ipsum dolor sit amet, consect etur adipiscing elit, sed do eiusmod tempor incididunt ut labore et dolore magna aliqua veniam....</p>
<p class="side-copy" style="top:1332px">Lorem ipsum dolor sit amet, consect etur adipiscing elit, sed do eiusmod tempor incididunt ut labore et dolore magna aliqua....</p>
<p class="side-copy" style="top:1433px">Lorem ipsum dolor sit amet, consect etur adipiscing elit, sed do eiusmod tempor incididunt ut labore et dolore magna aliqua....</p>
<span class="more" style="left:1072px;top:1530px">READ MORE</span>

<h2 class="band right" style="left:837px;top:1583px;width:329px">NEW DESIGN</h2>
<p class="side-copy" style="left:855px;top:1631px;width:290px">Lorem ipsum dolor sit amet, ncididunt ut magna aliqua....</p>
<div class="email-field" style="left:855px;top:1679px;width:280px;height:26px;padding-top:3px">Enter Your Email Address</div>
<span class="more" style="left:954px;top:1715px;border:none">SUBSCRIBE</span>
<span class="social" style="left:849px;background:#2f5fb0"></span>
<span class="social" style="left:900px;background:#3aa3e0"></span>
<span class="social" style="left:951px;background:#ef8a1c"></span>
<span class="social" style="left:1003px;background:#d9d9e6"></span>
<span class="social" style="left:1055px;background:#3c9a3c"></span>
<span class="social" style="left:1107px;background:#c4c8d8"></span>

<!-- footer -->
<footer class="site-footer"></footer>
<span class="foot-title" style="left:67px">WANT TO BECOME A PARTNER ?</span>
<span class="foot-title" style="left:450px">RESELLERS AND AGENTS</span>
<span class="foot-title" style="left:842px">TARVELLE WORLDWIDE</span>
<p class="foot-copy" style="left:70px;top:1914px;width:240px">Lorem ipsum dolor sit amet, consect etur adipiscing elit....</p>
<div class="email-field" style="left:70px;top:1960px;width:183px;height:26px;background:#1c1c24;border:none">Enter Your Email Address</div>
<div class="email-field" style="left:70px;top:1995px;width:183px;height:26px;background:#1c1c24;border:none">Enter Your Password</div>
<span class="foot-title" style="left:276px;top:1999px">SUBMIT</span>
<p class="foot-copy" style="left:452px;top:1914px;width:290px">Lorem ipsum dolor sit amet, consect etur adipiscing elit, sed do eiusmod tempor incididunt ut magna aliqua....</p>
<p class="foot-copy" style="left:452px;top:1989px;width:290px">Lorem ipsum dolor sit amet, consect etur adipiscing elit, sed do eiusmod tempor incididunt ut magna aliqua....</p>
<div class="map" role="img" aria-label="Street map showing the distributor location"></div>

<div class="bottom-bar">
  <p style="position:absolute;top:20px;width:100%">Privacy statement &nbsp;|&nbsp; Terms and Conditions &nbsp;|&nbsp; Sitemap</p>
  <p style="position:absolute;top:49px;width:100%">Copyright @ 2011 TARVELLE Crystal.com. All Rights Reserved.</p>
</div>

</body>
</html>
```